Fresh Compass Guide - Life coaching program for young people

Life coaching program for young people, A 4 triple fold like it to bright and fun with headings on each page
Front page photo of young people in a life coaching program with company logo , inside first The Program 2nd page What is Life Coaching
3rd Page About Your Life Coach
Outside 1st Page Testimonials 2nd outside page contact page 3 page Title page

Target Market(s)

Young People. Parents and Schools

Industry/Entity Type

Life Coaching

Font styles to use
Serif

Colors
0255a3
3276b5
85acd3
edf2f7
cee9f5

Requirements
Must have
• Lots of colour and be fun to look at but professional
Nice to have
• Fun Graphic headings good use of photos
• would like to focus on design then put in the words to fit area put aside for information
Should not have
• too many words

```html
<!DOCTYPE html>
<html lang="en">
<head>
<meta charset="utf-8">
<title>Fresh Compass Guide – Brochure Outside Spread</title>
<link rel="stylesheet" href="https://fonts.googleapis.com/css2?family=Cinzel:wght@600&family=Open+Sans:wght@400;600&display=swap">
<style>
  :root {
    --blue-deep: #0255a3;
    --blue-mid: #3276b5;
    --blue-soft: #85acd3;
    --blue-mist: #edf2f7;
    --blue-ice: #cee9f5;
    --ink-blue: #1a4f95;
    --orange: #d9542b;
    --white: #ffffff;
    --stage: #e4e7eb;
  }
  * { margin: 0; padding: 0; box-sizing: border-box; }
  html, body { width: 1200px; height: 800px; overflow: hidden; }
  body { background: var(--stage); font-family: "Open Sans", Arial, sans-serif; }

  .brochure {
    position: absolute; left: 45px; top: 30px;
    width: 1110px; height: 740px; overflow: hidden;
    box-shadow: 0 6px 18px rgba(0,0,0,.18);
  }
  .panel { position: absolute; top: 0; width: 370px; height: 740px; }
  .panel--testimonials { left: 0; background: var(--white); }
  .panel--contact { left: 370px; background: var(--blue-deep); }
  .panel--title { left: 740px; background: var(--white); }

  .photo-layer { position: absolute; inset: 0; width: 1110px; height: 740px; pointer-events: none; }
  .text-layer { position: absolute; inset: 0; width: 1110px; height: 740px; }

  /* Testimonials */
  .section-heading {
    position: absolute; left: 40px; top: 36px;
    font-family: "Cinzel", Georgia, serif; font-weight: 600;
    font-size: 17px; color: var(--ink-blue); letter-spacing: .5px;
  }
  .comment-list { position: absolute; left: 42px; top: 68px; width: 280px; }
  .comment {
    position: relative; background: var(--blue-soft);
    border-radius: 14px; padding: 6px 16px 8px;
    margin-bottom: 16px; width: 250px;
  }
  .comment:nth-child(even) { margin-left: 18px; }
  .comment::after {
    content: ""; position: absolute; right: 34px; bottom: -11px;
    border-left: 13px solid transparent; border-top: 12px solid var(--blue-soft);
  }
  .comment__name {
    font-family: "Cinzel", Georgia, serif; font-weight: 600; font-size: 13.5px;
    color: var(--ink-blue); border-bottom: 1px solid var(--blue-mist);
    padding-bottom: 2px; margin-bottom: 3px;
  }
  .comment__quote { font-size: 12px; line-height: 1.35; color: var(--white); }

  /* Contact */
  .brand {
    display: flex; align-items: center; justify-content: center; gap: 10px;
    font-family: "Cinzel", Georgia, serif; font-weight: 600;
  }
  .brand__dot { width: 18px; height: 18px; border-radius: 50%; flex: none; }
  .panel--contact .brand { position: absolute; top: 470px; left: 0; width: 100%; color: var(--white); font-size: 22px; }
  .panel--contact .brand__dot { background: var(--white); }
  .contact-info { position: absolute; top: 555px; width: 100%; text-align: center; color: var(--white); }
  .contact-info__heading { font-weight: 600; font-size: 14px; margin-bottom: 14px; }
  .contact-info__line { font-size: 13px; line-height: 1.6; }

  /* Title */
  .panel--title .brand { position: absolute; top: 562px; left: 0; width: 100%; color: var(--ink-blue); font-size: 21px; }
  .panel--title .brand__dot { background: var(--orange); }
  .services {
    position: absolute; top: 612px; width: 100%; text-align: center;
    font-family: "Cinzel", Georgia, serif; font-weight: 600;
    font-size: 12.5px; line-height: 1.45; color: var(--ink-blue);
  }
  .phone-band {
    position: absolute; left: 0; bottom: 0; width: 100%; height: 50px;
    background: var(--orange); color: var(--white);
    font-family: "Cinzel", Georgia, serif; font-weight: 600; font-size: 14px;
    display: flex; align-items: center; justify-content: center; letter-spacing: .5px;
  }
</style>
</head>
<body>
<main class="brochure">

  <section class="panel panel--testimonials"></section>
  <section class="panel panel--contact"></section>
  <section class="panel panel--title"></section>

  <svg class="photo-layer" viewBox="0 0 1110 740" xmlns="http://www.w3.org/2000/svg">
    <defs>
      <linearGradient id="photo-students" x1="0" y1="0" x2="1" y2="1">
        <stop offset="0" stop-color="#d6e6ef"/><stop offset="1" stop-color="#8fb8cf"/>
      </linearGradient>
      <linearGradient id="photo-group" x1="0" y1="0" x2="0" y2="1">
        <stop offset="0" stop-color="#ffffff"/><stop offset=".25" stop-color="#e3ecf3"/><stop offset="1" stop-color="#9fb8cc"/>
      </linearGradient>
      <linearGradient id="photo-coach" x1="0" y1="0" x2="0" y2="1">
        <stop offset="0" stop-color="#dfe6ec"/><stop offset="1" stop-color="#4a5566"/>
      </linearGradient>
      <linearGradient id="photo-paint" x1="0" y1="0" x2="1" y2="1">
        <stop offset="0" stop-color="#f1d9c8"/><stop offset="1" stop-color="#c9b7d9"/>
      </linearGradient>
    </defs>

    <rect x="0" y="585" width="370" height="155" fill="url(#photo-group)" role="img" aria-label="Photo of three smiling school students with backpacks"/>

    <circle cx="880" cy="115" r="295" fill="var(--blue-soft)"/>
    <g role="img" aria-label="Photo of two young students holding colourful folders">
      <circle cx="918" cy="95" r="245" fill="url(#photo-students)"/>
    </g>

    <circle cx="815" cy="455" r="74" fill="var(--orange)"/>
    <g role="img" aria-label="Photo of the life coach in a suit holding an award">
      <circle cx="815" cy="455" r="63" fill="url(#photo-coach)"/>
    </g>
    <circle cx="985" cy="375" r="58" fill="var(--orange)"/>
    <g role="img" aria-label="Photo of children showing paint-covered hands">
      <circle cx="985" cy="375" r="48" fill="url(#photo-paint)"/>
    </g>
  </svg>

  <div class="text-layer">
    <div class="panel panel--testimonials" style="background:none">
      <h2 class="section-heading">Young People’s Comments</h2>
      <div class="comment-list">
        <div class="comment"><p class="comment__name">Chloe:</p><p class="comment__quote">“ I didn’t know what a goal was until I did this program ”</p></div>
        <div class="comment"><p class="comment__name">Tom:</p><p class="comment__quote">“ My folks got shocked when I cleaned up my room without being asked ”</p></div>
        <div class="comment"><p class="comment__name">Sara:</p><p class="comment__quote">“ I have more confidence now ”</p></div>
        <div class="comment"><p class="comment__name">Emma:</p><p class="comment__quote">“ I learned people are all different but also the same ”</p></div>
        <div class="comment"><p class="comment__name">Nick:</p><p class="comment__quote">“ I want to do another program like this ”</p></div>
        <div class="comment"><p class="comment__name">Lisa:</p><p class="comment__quote">“ I can talk to people better now ”</p></div>
      </div>
    </div>

    <div class="panel panel--contact" style="background:none">
      <div class="brand"><span class="brand__dot"></span><span class="brand__name">Fresh Compass Guide</span></div>
      <div class="contact-info">
        <p class="contact-info__heading">Further Information</p>
        <p class="contact-info__line">Phone: 041-555-0192</p>
        <p class="contact-info__line">Email: hello@freshcompass.example</p>
      </div>
    </div>

    <div class="panel panel--title" style="background:none">
      <div class="brand"><span class="brand__dot"></span><span class="brand__name">Fresh Compass Guide</span></div>
      <p class="services">Individual or Group Coaching<br>Short Term or Long Term Programs<br>Daniel Hartley</p>
      <p class="phone-band">Phone: 041-555-0192</p>
    </div>
  </div>

</main>
</body>
</html>
```